Professional Services (B-2-B) Business Cards (Front & Back)

Quintarion is a business-to-business professional services company in the legal sector. They typically present to c-suite and executive functions who are looking for providers with expertise, and experience. Our business card should look and feel professional and contemporary, but we are not a startup tech company, so we want the tone to be more mature.

```html
<!DOCTYPE html>
<html lang="en">
<head>
<meta charset="utf-8">
<title>Quintarion Business Cards</title>
<link href="https://fonts.googleapis.com/css2?family=Montserrat:wght@400;500;800&display=swap" rel="stylesheet">
<style>
  :root {
    --navy: #1b3d73;
    --icon-blue: #2a86cc;
    --card-light: #eceff0;
    --card-edge: #c6c8ca;
    --canvas: #e2e4e6;
    --white: #ffffff;
  }
  * { box-sizing: border-box; margin: 0; padding: 0; }
  html, body {
    width: 1200px;
    height: 1200px;
    overflow: hidden;
    background: var(--canvas);
    font-family: "Montserrat", Arial, sans-serif;
  }
  .canvas {
    position: relative;
    width: 1200px;
    height: 1200px;
  }
  .card {
    position: absolute;
    left: 160px;
    width: 880px;
    height: 500px;
  }
  .card--front {
    top: 80px;
    background: var(--card-light);
    border: 1px solid var(--card-edge);
    color: var(--navy);
  }
  .card--back {
    top: 620px;
    background: var(--navy);
    display: flex;
    align-items: center;
    justify-content: center;
  }
  .identity {
    position: absolute;
    top: 118px;
    left: 0;
    right: 0;
    text-align: center;
  }
  .identity__name {
    font-weight: 800;
    font-size: 58px;
    line-height: 1;
    letter-spacing: 0.01em;
  }
  .identity__title {
    font-weight: 500;
    font-size: 30px;
    margin-top: 8px;
  }
  .contacts {
    position: absolute;
    top: 322px;
    left: 0;
    right: 0;
    display: grid;
    grid-template-columns: repeat(3, 1fr);
    padding: 0 6px;
  }
  .contact {
    display: flex;
    flex-direction: column;
    align-items: center;
    text-align: center;
  }
  .contact__icon {
    width: 36px;
    height: 36px;
    margin-bottom: 26px;
  }
  .contact__text {
    font-size: 21px;
    font-weight: 400;
    line-height: 1.35;
  }
  .brand {
    display: flex;
    align-items: center;
    gap: 28px;
    color: var(--white);
    margin-top: -40px;
  }
  .brand__mark {
    width: 44px;
    height: 44px;
    background: var(--white);
  }
  .brand__name {
    font-weight: 500;
    font-size: 38px;
    letter-spacing: 0.38em;
  }
</style>
</head>
<body>
<main class="canvas">
  <section class="card card--front" aria-label="Card front">
    <div class="identity">
      <h1 class="identity__name">MARA ELLISON</h1>
      <p class="identity__title">President &amp; CEO</p>
    </div>
    <div class="contacts">
      <div class="contact">
        <svg class="contact__icon" viewBox="0 0 24 24" fill="none" stroke="var(--icon-blue)" stroke-width="1.4" stroke-linejoin="round">
          <path d="M5 3.5 L8.2 3 L10 7.5 L8 9.2 C9.2 11.8 11.6 14.3 14.6 15.9 L16.4 14 L21 15.8 L20.5 19.2 C20.3 20.3 19.4 21 18.3 20.9 C10.4 20.2 3.8 13.6 3.1 5.7 C3 4.6 3.9 3.7 5 3.5 Z"/>
        </svg>
        <p class="contact__text">(415) 555 – 0142<br>(203) 555 – 0187</p>
      </div>
      <div class="contact">
        <svg class="contact__icon" viewBox="0 0 24 24" fill="none" stroke="var(--icon-blue)" stroke-width="1.4" stroke-linejoin="round">
          <rect x="2.5" y="5.5" width="19" height="13"/>
          <path d="M2.5 5.5 L12 13 L21.5 5.5"/>
        </svg>
        <p class="contact__text">mellison@quintarion.tech</p>
      </div>
      <div class="contact">
        <svg class="contact__icon" viewBox="0 0 24 24" fill="none" stroke="var(--icon-blue)" stroke-width="1.4">
          <circle cx="12" cy="12" r="9.5"/>
          <ellipse cx="12" cy="12" rx="4.5" ry="9.5"/>
          <path d="M2.5 12 H21.5 M4 7 H20 M4 17 H20 M12 2.5 V21.5"/>
        </svg>
        <p class="contact__text">www.quintarion.tech</p>
      </div>
    </div>
  </section>

  <section class="card card--back" aria-label="Card back">
    <div class="brand">
      <span class="brand__mark"></span>
      <span class="brand__name">QUINTARION</span>
    </div>
  </section>
</main>
</body>
</html>
```